Harlow & Pike Business Cards

I already have an existing logo but would like business cards as a compliment. New business looking to to buy and hold residential properties and wholesale real estate properties as well. I do not have an existing tag line, but I am working on something simple to incorporate.

Target Market(s)

Homeowners looking to sell

Contact Information for Business Card

Morvina T. Harlow
harlowandpike@mailvale.net

P.O. Box 812
Corvane, GA 30417

470.618.2093

Font styles to use
Serif

Requirements
Must have
• Tag line “ Selling Made Simple”
Nice to have
• I’m open to all things creative
Should not have
• No black background

```html
<!DOCTYPE html>
<html lang="en">
<head>
<meta charset="utf-8">
<title>Harlow &amp; Pike Business Cards</title>
<link rel="stylesheet" href="https://fonts.googleapis.com/css2?family=Arimo:wght@400;700&display=swap">
<style>
  :root {
    --navy: #2b1f7a;
    --navy-deep: #241a68;
    --gold: #c99a2e;
    --paper: #f4f4f6;
    --ink: #3a3296;
    --muted: #555560;
    --stage: #e6e6ea;
  }
  * { margin: 0; padding: 0; box-sizing: border-box; }
  html, body {
    width: 1200px; height: 997px; overflow: hidden;
    background: var(--stage);
    font-family: "Arimo", Arial, sans-serif;
  }
  .sheet {
    width: 1200px; height: 997px;
    display: flex; align-items: center; justify-content: center; gap: 90px;
  }
  .card {
    width: 380px; height: 664px;
    box-shadow: 0 14px 34px rgba(0,0,0,.22);
    position: relative; overflow: hidden;
  }
  .brand { display: flex; align-items: center; gap: 12px; }
  .brand-dot { width: 16px; height: 16px; border-radius: 50%; background: var(--gold); flex: none; }
  .brand-name {
    font-weight: 700; color: var(--gold); letter-spacing: 1px;
    text-transform: uppercase; white-space: nowrap;
  }

  /* Front card */
  .card-front { background: var(--paper); display: flex; flex-direction: column; }
  .front-band {
    height: 190px; background: var(--navy);
    display: flex; align-items: center; justify-content: center;
  }
  .card-front .brand-name { font-size: 28px; }
  .front-foot { height: 26px; background: var(--navy); margin-top: auto; }
  .contact {
    flex: 1; display: flex; flex-direction: column; align-items: center;
    padding-top: 34px; color: var(--ink); text-align: center;
  }
  .person-name { font-size: 23px; font-weight: 700; }
  .person-role { font-size: 15px; margin-top: 4px; color: var(--muted); }
  .contact-list {
    list-style: none; margin-top: 20px;
    display: flex; flex-direction: column; gap: 16px; align-items: center;
  }
  .contact-item { display: flex; flex-direction: column; align-items: center; gap: 8px; font-size: 17px; }
  .contact-icon {
    width: 44px; height: 44px; border-radius: 50%;
    background: var(--gold); border: 4px solid var(--navy);
    display: flex; align-items: center; justify-content: center;
  }
  .contact-icon svg { width: 20px; height: 20px; fill: var(--paper); }

  /* Back card */
  .card-back {
    background: linear-gradient(160deg, var(--navy) 0%, var(--navy-deep) 100%);
    display: flex; flex-direction: column; align-items: center;
  }
  .card-back .brand { margin-top: 225px; }
  .card-back .brand-name { font-size: 32px; }
  .tagline {
    margin-top: auto; margin-bottom: 72px;
    font-size: 25px; font-weight: 700; color: var(--gold);
    letter-spacing: .5px; text-transform: uppercase; white-space: nowrap;
  }
</style>
</head>
<body>
<main class="sheet">
  <section class="card card-front" aria-label="Business card front">
    <header class="front-band">
      <div class="brand"><span class="brand-dot"></span><span class="brand-name">Harlow &amp; Pike</span></div>
    </header>
    <div class="contact">
      <p class="person-name">Morvina T. Harlow</p>
      <p class="person-role">Director</p>
      <ul class="contact-list">
        <li class="contact-item">
          <span class="contact-icon"><svg viewBox="0 0 24 24"><path d="M6.6 10.8a15 15 0 0 0 6.6 6.6l2.2-2.2a1 1 0 0 1 1-.25 11.4 11.4 0 0 0 3.6.57 1 1 0 0 1 1 1V20a1 1 0 0 1-1 1A17 17 0 0 1 3 4a1 1 0 0 1 1-1h3.5a1 1 0 0 1 1 1c0 1.25.2 2.45.57 3.57a1 1 0 0 1-.25 1z"/></svg></span>
          <span>470.618.2093</span>
        </li>
        <li class="contact-item">
          <span class="contact-icon"><svg viewBox="0 0 24 24"><path d="M3 5h18v14H3z M3 5l9 7 9-7" stroke="#2b1f7a" stroke-width="1.6"/></svg></span>
          <span>harlowandpike@mailvale.net</span>
        </li>
        <li class="contact-item">
          <span class="contact-icon"><svg viewBox="0 0 24 24"><path d="M12 2a7 7 0 0 0-7 7c0 5 7 13 7 13s7-8 7-13a7 7 0 0 0-7-7zm0 9.5A2.5 2.5 0 1 1 12 6.5a2.5 2.5 0 0 1 0 5z"/></svg></span>
          <span>P.O. Box 812 Corvane, GA 30417</span>
        </li>
      </ul>
    </div>
    <footer class="front-foot"></footer>
  </section>

  <section class="card card-back" aria-label="Business card back">
    <div class="brand"><span class="brand-dot"></span><span class="brand-name">Harlow &amp; Pike</span></div>
    <p class="tagline">Selling Made Simple</p>
  </section>
</main>
</body>
</html>
```